Sturdyflow Mechanical - Letterhead

We are a plumbing and hvac company based in Calgary. This letterhead will be on our quotes, invoices, preventative maintenance proposals etc.

```html
<!DOCTYPE html>
<html lang="en">
<head>
<meta charset="utf-8">
<title>Sturdyflow Mechanical – Letterhead</title>
<link href="https://fonts.googleapis.com/css2?family=Open+Sans:wght@400;600;700&display=swap" rel="stylesheet">
<style>
  :root {
    --brand-blue: #1f6bb5;
    --brand-orange: #e4561f;
    --ink: #4a4a4a;
    --ink-soft: #6b6b6b;
    --paper: #ffffff;
    --backdrop: #eceef0;
    --mark-tint: #f6ecea;
    --signature-tint: #e6e6e6;
  }
  * { box-sizing: border-box; margin: 0; padding: 0; }
  html, body {
    width: 1200px; height: 800px; overflow: hidden;
    background: var(--backdrop);
    font-family: "Open Sans", Arial, sans-serif;
  }
  .letterhead {
    position: absolute; left: 306px; top: 20px;
    width: 588px; height: 760px;
    background: var(--paper);
    overflow: hidden;
    box-shadow: 0 2px 10px rgba(0,0,0,0.08);
  }
  .brand {
    position: absolute; left: 44px; top: 44px;
    display: flex; align-items: center; gap: 8px;
    color: var(--brand-blue);
    font-weight: 700; font-size: 17px; letter-spacing: 0.3px;
  }
  .brand-dot {
    width: 14px; height: 14px; border-radius: 50%;
    background: var(--brand-orange);
  }
  .contact {
    position: absolute; left: 404px; top: 104px;
    width: 164px;
    padding-left: 12px;
    border-left: 2px solid var(--brand-blue);
    font-style: normal;
    font-size: 9.5px; font-weight: 600; line-height: 14px;
    color: var(--ink);
  }
  .contact-line { display: flex; align-items: center; gap: 5px; }
  .contact-icon { width: 8px; height: 8px; flex: none; }
  .letter {
    position: absolute; left: 44px; top: 206px; width: 500px;
    font-size: 10px; line-height: 1.5; color: var(--ink-soft);
  }
  .greeting { margin-bottom: 10px; }
  .letter p { margin-bottom: 10px; }
  .closing { margin-top: 4px; }
  .signature {
    width: 90px; height: 44px; margin-top: 12px;
    background: var(--signature-tint); border-radius: 4px;
  }
  .backmark {
    position: absolute; right: 60px; bottom: 30px;
    width: 240px; height: 240px; border-radius: 50%;
    background: var(--mark-tint); opacity: 0.6;
    z-index: 0;
  }
  .letter, .contact, .brand { z-index: 1; }
  .footer-band-blue {
    position: absolute; left: 0; bottom: 0;
    width: 64%; height: 7px; background: var(--brand-blue);
  }
  .footer-band-orange {
    position: absolute; right: 0; bottom: 0;
    width: 35%; height: 12px; background: var(--brand-orange);
  }
</style>
</head>
<body>
  <main class="letterhead">
    <div class="backmark" role="img" aria-label="Faint brand symbol decoration"></div>

    <header class="brand">
      <span class="brand-dot" aria-hidden="true"></span>
      <span class="brand-name">STURDYFLOW MECHANICAL INC</span>
    </header>

    <address class="contact">
      <div>2150 Crowchild Trail NW,</div>
      <div>Suite 310 Calgary.</div>
      <div class="contact-line">
        <svg class="contact-icon" viewBox="0 0 10 10"><path d="M2 1 L4 1 L4.6 3 L3.4 3.8 Q4.4 5.8 6.2 6.6 L7 5.4 L9 6 L9 8 Q5 9 1.6 5 Q1 3 2 1Z" fill="var(--brand-orange)"/></svg>
        <span>403.555.0182</span>
      </div>
      <div class="contact-line">
        <svg class="contact-icon" viewBox="0 0 10 10"><rect x="0.5" y="2" width="9" height="6.5" rx="1" fill="var(--brand-orange)"/><path d="M1 2.6 L5 5.6 L9 2.6" stroke="#fff" stroke-width="0.9" fill="none"/></svg>
        <span>info@sturdyflow.ca</span>
      </div>
      <div class="contact-line">
        <svg class="contact-icon" viewBox="0 0 10 10"><circle cx="5" cy="5" r="4.5" fill="var(--brand-orange)"/><path d="M0.8 5 H9.2 M5 0.6 Q2.5 5 5 9.4 M5 0.6 Q7.5 5 5 9.4" stroke="#fff" stroke-width="0.7" fill="none"/></svg>
        <span>www.sturdyflow.ca</span>
      </div>
    </address>

    <section class="letter">
      <div class="greeting">Dear customer,</div>
      <p>Lorem ipsum dolor sit amet, consectetur adipisicing elit, sed do eiusmod tempor incididunt ut labore et dolore magna aliqua. Ut enim ad minim veniam, quis nostrud exercitation ullamco laboris nisi ut aliquip ex ea commodo consequat. Duis aute irure dolor in reprehenderit in voluptate velit esse cillum dolore eu fugiat nulla pariatur. Excepteur sint occaecat cupidatat non proident, sunt in culpa qui officia deserunt mollit anim id est laborum.</p>
      <p>Lorem ipsum dolor sit amet, consectetur adipisicing elit, sed do eiusmod tempor incididunt ut labore et dolore magna aliqua. Ut enim ad minim veniam, quis nostrud exercitation ullamco laboris nisi ut aliquip ex ea commodo consequat. Duis aute irure dolor in reprehenderit in voluptate velit esse cillum dolore eu fugiat nulla pariatur. Excepteur sint occaecat cupidatat non proident, sunt in culpa qui officia deserunt mollit anim id est laborum.</p>
      <p>Lorem ipsum dolor sit amet, consectetur adipisicing elit, sed do eiusmod tempor incididunt ut labore et dolore magna aliqua. Ut enim ad minim veniam, quis nostrud exercitation ullamco laboris nisi ut aliquip ex ea commodo consequat. Duis aute irure dolor in reprehenderit in voluptate velit esse cillum dolore eu fugiat nulla pariatur. Excepteur sint occaecat cupidatat non proident, sunt in culpa qui officia deserunt mollit anim id est laborum.</p>
      <p>Lorem ipsum dolor sit amet, consectetur adipisicing elit, sed do eiusmod tempor incididunt ut labore et dolore magna aliqua. Ut enim ad minim veniam, quis nostrud exercitation ullamco laboris nisi ut aliquip ex ea commodo consequat. Duis aute irure dolor in reprehenderit.</p>
      <div class="closing">Yours Sincerely,</div>
      <div class="signature" role="img" aria-label="Handwritten signature"></div>
    </section>

    <div class="footer-band-blue" aria-hidden="true"></div>
    <div class="footer-band-orange" aria-hidden="true"></div>
  </main>
</body>
</html>
```